Aquaponic greenhouse needs a business brochure that shows what a unique system we have

We would like to expand our marketing beyond social media. We are a aquaponic greenhouse where we use fish to fertilize the water so that we don't have to use any chemicals in the system. This method is sustainable and environmentally friendly. We grow in a climate controlled system year round and deliver the freshest produce directly to our local families, schools and restaurants. All of our produce is grown from seed, closely monitored during the growing cycle, hand picked and hand packaged for our customers.

Aquaponics - The combination of Aquaculture (raising fish) and Hydroponics (growing plants in a soilless system)

Sustainable - Closed loop system using the same water for the fish and plants.

Local - Delaware natives providing healthy eating opportunities for our neighbors throughout the state.

Chemical and Soil Free

Largest in the First State - With over 15,000 square feet of a climate controlled environment, we can grow the freshest produce year round with consistent output.

Target Market(s)

Customers and those who don’t use social media

Industry/Entity Type

Agribusiness

Font styles to use
Sans Serif

Colors
0255a3
32b8a4
9bcb3c
cadf82

Requirements
Must have
• Our logo (attached) some personalized pictures (can be found on our website www.quillmeadowgrow.com) and areas where we can customize our written content. Must have editable text and be able to replace pictures as we grow.
Nice to have
• Options for a tri-fold and bi-fold brochures

```html
<!DOCTYPE html>
<html lang="en">
<head>
<meta charset="utf-8">
<title>Quill Meadow Grow – Tri-fold Brochure</title>
<link href="https://fonts.googleapis.com/css2?family=Open+Sans:wght@400;600;700;800&display=swap" rel="stylesheet">
<style>
:root{
  --blue:#0255a3;
  --blue-deep:#013d7a;
  --blue-light:#2a86d1;
  --teal:#32b8a4;
  --green:#9bcb3c;
  --green-mid:#5fae35;
  --green-dark:#3f8f2a;
  --lime:#cadf82;
  --white:#ffffff;
  --ink:#2b3a4a;
  --bg:#e4e5e7;
  --photo-leaf:#4f8a3a;
  --photo-glass:#9fb7c4;
}
*{box-sizing:border-box;margin:0;padding:0}
html,body{width:1200px;height:2400px;overflow:hidden}
body{background:var(--bg);font-family:"Open Sans",Arial,sans-serif;color:var(--ink);position:relative}

.spread{position:absolute;left:45px;width:1110px;height:858px;display:flex;box-shadow:0 10px 30px rgba(0,0,0,.18);background:var(--white)}
.spread--outside{top:190px}
.spread--inside{top:1250px}
.panel{position:relative;width:370px;height:858px;overflow:hidden}
.wide-panel{position:relative;width:740px;height:858px;overflow:hidden}
.abs{position:absolute}
svg.abs{display:block}

.photo{position:absolute}
.photo--fish{background:radial-gradient(circle at 40% 45%,#d8b9a2 0,#a77a63 30%,#3d4a4a 75%)}
.photo--greenhouse{background:linear-gradient(180deg,var(--photo-glass) 0%,#7a9a8a 30%,var(--photo-leaf) 55%,#2f5f2a 100%)}
.photo--grower{background:linear-gradient(160deg,#a8bfcc 0%,#6f8fa0 30%,#4d8a3c 60%,#2e6a2a 100%)}
.photo--van{background:linear-gradient(180deg,#cfe0ea 0%,#8fb7c9 45%,#3d7a9e 100%)}
.photo--rows{background:linear-gradient(180deg,#b7c9cf 0%,#5f9a46 40%,#2f6a2a 100%)}
.photo--lettuce{background:radial-gradient(circle at 50% 55%,#8fd05a 0,#4c9a32 55%,transparent 72%)}
.photo--circle{border-radius:50%;border:5px solid var(--white);box-shadow:0 3px 8px rgba(0,0,0,.25)}

.brand{display:flex;align-items:center;gap:10px}
.brand__dot{width:18px;height:18px;border-radius:50%;background:var(--green)}
.brand__name{font-weight:800;color:var(--blue);text-transform:uppercase;letter-spacing:.5px;line-height:1}

.heading{font-weight:800;text-transform:uppercase;line-height:1.15}
.copy{font-size:10.5px;line-height:1.5}

.pill{position:absolute;display:flex;align-items:center;justify-content:center;gap:8px;background:var(--green);color:var(--white);font-weight:700;border-radius:20px;height:34px;font-size:16px}
.pill svg{width:15px;height:15px}

/* outside: why panel */
.why__title{position:absolute;left:34px;top:128px;font-size:17px;color:var(--blue)}
.why__list{position:absolute;left:30px;top:162px;width:310px;list-style:none}
.why__list li{position:relative;padding-left:18px;font-size:10.5px;line-height:1.45;margin-bottom:9px;color:#44505c}
.why__list li::before{content:"";position:absolute;left:0;top:4px;width:9px;height:9px;border-radius:50%;background:var(--blue)}

/* outside: green panel */
.panel--green{background:linear-gradient(180deg,var(--green-mid) 0%,var(--green) 100%)}
.green__lead{position:absolute;left:30px;right:30px;top:232px;text-align:center;color:var(--white);font-size:15px}
.green__box{position:absolute;left:30px;right:30px;top:318px;border:2px solid var(--white);padding:12px 10px;text-align:center;color:var(--white);font-size:15px}
.green__largest{position:absolute;left:30px;right:30px;top:430px;text-align:center;color:var(--white)}
.green__largest .heading{font-size:15px;display:flex;justify-content:center;align-items:center;gap:8px}
.green__largest .copy{font-size:12px;margin-top:6px}
.contact{position:absolute;left:0;right:0;top:660px;text-align:center;color:var(--white)}
.social{display:flex;justify-content:center;gap:12px;margin-bottom:14px}
.social span{width:24px;height:24px;border-radius:50%;background:var(--green)}
.contact__address{font-size:12px;line-height:1.4}
.contact__web{font-size:17px;font-weight:700;margin-top:8px}

/* cover */
.cover__headline{position:absolute;left:20px;right:20px;top:690px;text-align:center;color:var(--white);font-size:21px}
.badge{position:absolute;border-radius:50%;background:var(--green-mid);border:4px solid var(--white);color:var(--white);display:flex;flex-direction:column;align-items:center;justify-content:center;text-align:center;font-weight:800;text-transform:uppercase;font-size:11px;line-height:1.2}

/* inside: first panel */
.climate__title{position:absolute;left:30px;top:46px;width:300px;font-size:17px;color:var(--green-dark)}
.climate__copy{position:absolute;left:30px;top:100px;width:310px;color:#44505c}
.climate__copy p{margin-bottom:10px}
.features{position:absolute;left:30px;top:290px;width:310px;list-style:none}
.features li{position:relative;padding-left:30px;margin-bottom:11px}
.features .tick{position:absolute;left:0;top:0;width:20px;height:20px;border-radius:50%;background:var(--blue);display:flex;align-items:center;justify-content:center}
.features .tick svg{width:11px;height:11px}
.features h3{font-size:13px;font-weight:800;color:var(--blue);text-transform:uppercase}
.features p{font-size:10.5px;line-height:1.4;color:#44505c}

/* inside: wide panel */
.gh{position:absolute;left:30px;top:430px;width:310px;color:var(--white)}
.gh .heading{font-size:19px;margin-bottom:10px}
.gh .copy{margin-bottom:10px}
.gh__quote{position:relative;padding-left:26px;font-style:italic}
.gh__quote::before{content:"\201C";position:absolute;left:0;top:-10px;font-size:40px;font-weight:800;color:var(--green);font-style:normal}
.produce{position:absolute;left:400px;top:470px;width:310px;color:var(--white)}
.produce .heading{font-size:17px;margin-bottom:12px}
.produce ul{list-style:none}
.produce li{display:flex;align-items:baseline;font-size:12px;margin-bottom:12px}
.produce li .leader{flex:1;border-bottom:1px dotted rgba(255,255,255,.7);margin:0 6px}
.delivery-note{position:absolute;left:400px;top:740px;color:var(--green);font-weight:800;text-transform:uppercase;font-size:14px;line-height:1.2}
</style>
</head>
<body>

<!-- OUTSIDE SPREAD -->
<section class="spread spread--outside" aria-label="Brochure outside">

  <article class="panel panel--why">
    <svg class="abs" style="left:0;top:0" width="370" height="110" viewBox="0 0 370 110">
      <path d="M0 0H370V30C250 70 120 20 0 70Z" fill="var(--blue)"/>
      <path d="M0 70C120 20 250 70 370 30V44C250 84 120 34 0 84Z" fill="var(--green-mid)"/>
    </svg>
    <div class="brand abs" style="left:190px;top:80px"><span class="brand__dot"></span><span class="brand__name" style="font-size:15px">Quill Meadow Grow</span></div>
    <h2 class="heading why__title">Why Aquaponics?</h2>
    <ul class="why__list">
      <li>Fish feed the plants, so our water stays clean and free of added chemicals all season.</li>
      <li>Our greenhouse runs year round, giving steady harvests in every kind of weather.</li>
      <li>No soil and no sprays are used, so every leaf is clean when it reaches you.</li>
      <li>A closed loop saves water by sharing it between the fish and the plants.</li>
      <li>Produce is picked and packed by hand for local families and restaurants.</li>
      <li>Ask about weekly orders. We deliver fresh greens to your door.</li>
    </ul>
    <div class="photo photo--fish" style="left:0;top:470px;width:370px;height:320px" role="img" aria-label="Photo of tilapia swimming in the aquaponic fish tank"></div>
    <svg class="abs" style="left:0;top:740px" width="370" height="118" viewBox="0 0 370 118">
      <path d="M0 40C120 0 260 60 370 20V118H0Z" fill="var(--blue)"/>
    </svg>
  </article>

  <article class="panel panel--green">
    <div class="photo photo--van photo--circle" style="left:110px;top:40px;width:150px;height:150px" role="img" aria-label="Photo of the delivery van"></div>
    <p class="heading green__lead">Locally grown, sustainable produce including multiple varieties of lettuce</p>
    <p class="heading green__box">We offering personalized delivery on orders totaling $100 or more</p>
    <div class="green__largest">
      <p class="heading">Largest in the 1st State!
        <svg width="26" height="16" viewBox="0 0 26 16"><rect x="0" y="2" width="15" height="10" fill="var(--white)"/><path d="M15 5H21L25 9V12H15Z" fill="var(--white)"/><circle cx="5" cy="13" r="2.5" fill="var(--green-dark)"/><circle cx="20" cy="13" r="2.5" fill="var(--green-dark)"/></svg>
      </p>
      <p class="copy">With over 15,000 square feet of a climate controlled environment, we can grow the freshest produce year round with consistent output.</p>
    </div>
    <svg class="abs" style="left:0;top:560px" width="370" height="298" viewBox="0 0 370 298">
      <defs><linearGradient id="blueFade" x1="0" y1="0" x2="0" y2="1"><stop offset="0" stop-color="var(--blue-light)"/><stop offset="1" stop-color="var(--blue-deep)"/></linearGradient></defs>
      <path d="M0 50C130 0 250 80 370 30V298H0Z" fill="url(#blueFade)"/>
    </svg>
    <div class="contact">
      <div class="social"><span></span><span></span><span></span></div>
      <p class="contact__address">212 Harrow Field Rd,<br>Millbrook, US 00000</p>
      <p class="contact__web">www.quillmeadowgrow.com</p>
    </div>
    <div class="pill" style="left:75px;top:800px;width:220px">
      <svg viewBox="0 0 24 24"><path d="M6.6 10.8a15 15 0 0 0 6.6 6.6l2.2-2.2c.3-.3.7-.4 1-.2 1.1.4 2.3.6 3.6.6.6 0 1 .4 1 1V20c0 .6-.4 1-1 1A17 17 0 0 1 3 4c0-.6.4-1 1-1h3.5c.6 0 1 .4 1 1 0 1.3.2 2.5.6 3.6.1.3 0 .7-.2 1Z" fill="var(--white)"/></svg>
      (555) 014-2287
    </div>
  </article>

  <article class="panel panel--cover">
    <div class="photo photo--grower" style="left:0;top:150px;width:370px;height:480px" role="img" aria-label="Photo of a grower holding a raft of fresh lettuce in the greenhouse"></div>
    <svg class="abs" style="left:0;top:0" width="370" height="230" viewBox="0 0 370 230">
      <path d="M0 0H370V150C250 210 110 150 0 200Z" fill="var(--white)"/>
      <path d="M0 200C110 150 250 210 370 150V164C250 224 110 164 0 214Z" fill="var(--green-mid)"/>
    </svg>
    <div class="brand abs" style="left:50px;top:80px"><span class="brand__dot" style="width:26px;height:26px"></span><span class="brand__name" style="font-size:24px">Quill Meadow Grow</span></div>
    <svg class="abs" style="left:0;top:560px" width="370" height="298" viewBox="0 0 370 298">
      <defs><linearGradient id="blueFade2" x1="0" y1="0" x2="0" y2="1"><stop offset="0" stop-color="var(--blue-light)"/><stop offset="1" stop-color="var(--blue-deep)"/></linearGradient></defs>
      <path d="M0 90C140 20 260 70 370 0V298H0Z" fill="url(#blueFade2)"/>
      <path d="M0 90C140 20 260 70 370 0V10C260 80 140 30 0 100Z" fill="var(--white)"/>
    </svg>
    <div class="badge" style="left:240px;top:480px;width:110px;height:110px">
      <svg width="26" height="16" viewBox="0 0 26 16"><rect x="0" y="2" width="15" height="10" fill="var(--white)"/><path d="M15 5H21L25 9V12H15Z" fill="var(--white)"/><circle cx="5" cy="13" r="2.5" fill="var(--green-dark)"/><circle cx="20" cy="13" r="2.5" fill="var(--green-dark)"/></svg>
      Delivery on<br>orders<br>$100 or more
    </div>
    <h1 class="heading cover__headline">Aquaponic Greenhouse Climate Controlled System Year Round</h1>
    <div class="pill" style="left:75px;top:790px;width:220px">
      <svg viewBox="0 0 24 24"><path d="M6.6 10.8a15 15 0 0 0 6.6 6.6l2.2-2.2c.3-.3.7-.4 1-.2 1.1.4 2.3.6 3.6.6.6 0 1 .4 1 1V20c0 .6-.4 1-1 1A17 17 0 0 1 3 4c0-.6.4-1 1-1h3.5c.6 0 1 .4 1 1 0 1.3.2 2.5.6 3.6.1.3 0 .7-.2 1Z" fill="var(--white)"/></svg>
      (555) 014-2287
    </div>
  </article>
</section>

<!-- INSIDE SPREAD -->
<section class="spread spread--inside" aria-label="Brochure inside">

  <article class="panel panel--climate">
    <svg class="abs" style="left:0;top:0" width="370" height="40" viewBox="0 0 370 40">
      <path d="M0 0H370V10C240 30 120 0 0 24Z" fill="var(--blue)"/>
    </svg>
    <h2 class="heading climate__title">Climate Controlled System Year Round</h2>
    <div class="copy climate__copy">
      <p>We are a aquaponic greenhouse where we use fish to fertilize the water so that we don't have to use any chemicals in the system. This method is sustainable and environmentally friendly.</p>
      <p>We grow in a climate controlled system year round and deliver the freshest produce directly to our local families, schools and restaurants. All of our produce is grown from seed, closely monitored during the growing cycle, hand picked and hand packaged for our customers.</p>
    </div>
    <ul class="features">
      <li><span class="tick"><svg viewBox="0 0 12 12"><path d="M2 6.5L5 9.5L10 3" stroke="var(--white)" stroke-width="2" fill="none"/></svg></span><h3>Aquaponics</h3><p>The combination of Aquaculture (raising fish) and Hydroponics (growing plants in a soilless system).</p></li>
      <li><span class="tick"><svg viewBox="0 0 12 12"><path d="M2 6.5L5 9.5L10 3" stroke="var(--white)" stroke-width="2" fill="none"/></svg></span><h3>Sustainable</h3><p>Closed loop system using the same water for the fish and plants.</p></li>
      <li><span class="tick"><svg viewBox="0 0 12 12"><path d="M2 6.5L5 9.5L10 3" stroke="var(--white)" stroke-width="2" fill="none"/></svg></span><h3>Local</h3><p>Delaware natives providing healthy eating opportunities for our neighbors throughout the state.</p></li>
      <li><span class="tick"><svg viewBox="0 0 12 12"><path d="M2 6.5L5 9.5L10 3" stroke="var(--white)" stroke-width="2" fill="none"/></svg></span><h3>Chemical and Soil Free</h3></li>
    </ul>
    <div class="photo photo--rows" style="left:0;top:600px;width:370px;height:258px" role="img" aria-label="Photo of lettuce growing in rows of hydroponic towers"></div>
    <svg class="abs" style="left:0;top:590px" width="370" height="40" viewBox="0 0 370 40">
      <path d="M0 0H370V10C240 40 120 0 0 30Z" fill="var(--white)"/>
    </svg>
  </article>

  <article class="wide-panel panel--greenhouse">
    <div class="photo photo--greenhouse" style="left:0;top:0;width:740px;height:420px" role="img" aria-label="Photo of the greenhouse interior filled with leafy greens"></div>
    <svg class="abs" style="left:0;top:320px" width="740" height="538" viewBox="0 0 740 538">
      <defs><linearGradient id="blueFade3" x1="0" y1="0" x2="0" y2="1"><stop offset="0" stop-color="var(--blue-light)"/><stop offset="1" stop-color="var(--blue-deep)"/></linearGradient></defs>
      <path d="M0 90C220 20 480 110 740 30V538H0Z" fill="url(#blueFade3)"/>
      <path d="M0 80C220 10 480 100 740 20V34C480 114 220 24 0 94Z" fill="var(--white)"/>
    </svg>
    <div class="photo photo--greenhouse photo--circle" style="left:470px;top:300px;width:100px;height:100px" role="img" aria-label="Close-up photo of leafy greens"></div>
    <div class="photo photo--fish photo--circle" style="left:585px;top:290px;width:100px;height:100px" role="img" aria-label="Close-up photo of ripe tomatoes on the vine"></div>

    <div class="gh">
      <h2 class="heading">Aquaponic Greenhouses</h2>
      <p class="copy">Aquaponics is a system of soilless growing that uses fish to create a fertilizer that can be recycled continuously throughout the growing system.</p>
      <p class="copy gh__quote">We filter out the solids. There's a process of water going through a filtration system and then it goes into a nitrification tank where bacteria turn the waste into plant food. We then use that water for the plants and it returns clean back to you and the fish.</p>
      <p class="copy">The greens that the fish help to grow are Romaine, Summer Crisp and a Buttercrunch lettuce as well as a Spring Mix, which has a different variety of lettuces in it for a spring salad.</p>
    </div>
    <div class="pill" style="left:70px;top:790px;width:220px">
      <svg viewBox="0 0 24 24"><path d="M6.6 10.8a15 15 0 0 0 6.6 6.6l2.2-2.2c.3-.3.7-.4 1-.2 1.1.4 2.3.6 3.6.6.6 0 1 .4 1 1V20c0 .6-.4 1-1 1A17 17 0 0 1 3 4c0-.6.4-1 1-1h3.5c.6 0 1 .4 1 1 0 1.3.2 2.5.6 3.6.1.3 0 .7-.2 1Z" fill="var(--white)"/></svg>
      (555) 014-2287
    </div>

    <div class="produce">
      <h2 class="heading">Produce</h2>
      <ul>
        <li>Summer Crisp Lettuce<span class="leader"></span>$4.00</li>
        <li>Romaine Lettuce<span class="leader"></span>$4.00</li>
        <li>Wildfire Lettuce Mix<span class="leader"></span>$4.00</li>
        <li>Buttercrunch Lettuce<span class="leader"></span>$3.00</li>
        <li>Swiss Chard<span class="leader"></span>$3.00</li>
      </ul>
    </div>
    <div class="delivery-note">
      <svg width="26" height="16" viewBox="0 0 26 16"><rect x="0" y="2" width="15" height="10" fill="var(--green)"/><path d="M15 5H21L25 9V12H15Z" fill="var(--green)"/><circle cx="5" cy="13" r="2.5" fill="var(--blue-deep)"/><circle cx="20" cy="13" r="2.5" fill="var(--blue-deep)"/></svg><br>
      Delivery on<br>orders<br>$100 or more
    </div>
    <div class="photo photo--lettuce" style="left:560px;top:700px;width:160px;height:130px" role="img" aria-label="Photo of a fresh head of lettuce"></div>
  </article>
</section>

</body>
</html>
```